依頼詳細
【必ず入れて頂きたい要素】
①「アルコールと天然由来成分のチカラで室内除菌」というキャッチコピー。
②画像を使用し、キャッチコピーのイメージを入居者様が勝手に抱くデザイン。
※キャッチコピーとデザインで勝負し、下記の補足説明は可能な限り文字数を少なく、小さくする。

【補足説明として入れて頂きたい要素】
①「消臭・除菌施工サービス」というサービス名称。
②アルコールと国産の天然ひのきと緑茶エキスを使用。
③「中和反応法で悪臭の原因成分を分解」という事を添付画像「中和反応法」
のように図で説明。
④「第三者機関で効果を検証」という文言。
※添付画像「室内空気衛生推進連盟」のマークを挿入。

⑤2つの会社情報を記入するスペースを確保
1つは自由に社名や電話番号を記載できるように空欄とする
スペースのタイトルは「サービス提供会社」

1つは弊社の下記情報を記載
タイトルは「技術提供会社」
添付画像「会社ロゴ」
住所:東京都港区芝浦4-17-6森田ビル5F
電話:03-5871-2943
Mail:info@kt-planwork.jp
記載項目
株式会社住環境企画工房/東京都港区芝浦4-17-6森田ビル5F
電話:03-5871-2943/Mail:info@kt-planwork.jp
サイズ
A4
ページ数
片面
希望イメージ
シンプル 複雑
単色 カラフル
暗い 明るい
日常 高級
遊び心 厳粛
未来的 伝統的
女性的 男性的
希望する色
緑系、青系、水色系
納品ファイル
• 高解像度JPG (.jpg)
• イラストレーター形式 (.ai)
• PNG形式 (.png)
補足説明
下記3種のファイルでの納品お願い致します。
Ai(アウトライン前とアウトライン後)
PDF
jpg
(全てトンボ有り・無し両方)

```html
<!DOCTYPE html>
<html lang="ja">
<head>
<meta charset="utf-8">
<title>消臭・抗菌施工サービス｜2つのチカラで室内除菌</title>
<link href="https://fonts.googleapis.com/css2?family=Noto+Sans+JP:wght@400;500;700;900&display=swap" rel="stylesheet">
<style>
  :root{
    --blue-deep:#0d4f9c;
    --blue:#1a78c8;
    --blue-bright:#2e9be0;
    --sky:#cfe9f8;
    --sky-pale:#eaf5fc;
    --green:#6cb33f;
    --green-pale:#e4f2d8;
    --ink:#333a44;
    --gray:#f1f3f5;
    --line:#c9d6e2;
    --white:#ffffff;
    --gold:#f5c542;
  }
  *{box-sizing:border-box;margin:0;padding:0}
  html,body{width:846px;height:1200px;overflow:hidden;background:var(--white)}
  body{font-family:"Noto Sans JP",sans-serif;color:var(--ink)}
  .flyer{position:relative;width:846px;height:1200px;overflow:hidden;background:var(--white)}

  /* hero */
  .hero{position:absolute;left:0;top:0;width:846px;height:576px}
  .hero-photo{position:absolute;inset:0;
    background:linear-gradient(165deg,#f6f8fa 0%,#e3eef6 25%,#8fc3e8 48%,#4d9bd8 60%,#cfe4f3 80%,#a9d1ee 100%)}
  .service-badge{position:absolute;left:22px;top:20px;width:118px;padding:8px 0 10px;background:var(--blue-deep);color:var(--white);text-align:center;font-weight:700;font-size:14px;line-height:1.35}
  .service-badge .stars{color:var(--gold);font-size:13px;letter-spacing:2px;margin-bottom:2px}
  .hex-pair{position:absolute;left:330px;top:216px;width:250px;height:110px}
  .hex-pair svg{position:absolute;inset:0}
  .hex-label{position:absolute;font-weight:700;color:var(--blue);font-size:15px;text-align:center;line-height:1.25}
  .hex-label.alcohol{left:8px;top:44px;width:96px}
  .hex-label.natural{left:126px;top:18px;width:100px}
  .power-band{position:absolute;left:236px;top:344px;width:380px;height:48px;background:var(--blue-deep);transform:skewX(-12deg);display:flex;align-items:center;justify-content:center}
  .power-band span{transform:skewX(12deg);color:var(--white);font-weight:900;font-size:30px;letter-spacing:1px;line-height:1}
  .power-band em{font-style:normal;font-size:36px;color:#8fd3ff}
  .main-copy{position:absolute;left:0;top:418px;width:846px;text-align:center;font-weight:900;font-size:118px;line-height:1;letter-spacing:10px;color:var(--white);
    text-shadow:4px 0 0 var(--blue),-4px 0 0 var(--blue),0 4px 0 var(--blue),0 -4px 0 var(--blue),3px 3px 0 var(--blue),-3px 3px 0 var(--blue),3px -3px 0 var(--blue),-3px -3px 0 var(--blue),0 8px 14px rgba(13,79,156,.35)}

  /* photo row */
  .scene-row{position:absolute;left:0;top:576px;width:846px;height:140px;display:flex;gap:4px;background:var(--white)}
  .scene{flex:1}
  .scene.wipe{background:linear-gradient(135deg,#d9ecf7,#5fa8dc 60%,#f0c94a)}
  .scene.room{background:linear-gradient(180deg,#f7f4ee,#e6dccd 55%,#c9ab84)}
  .scene.family{background:linear-gradient(135deg,#fbf1ea,#eed3c3 55%,#f8f8f8)}

  /* ingredients */
  .ingredient-title{position:absolute;left:0;top:738px;width:846px;text-align:center;color:var(--blue);font-weight:700;font-size:25px;line-height:1.4}
  .ingredient-title::after{content:"";display:block;width:640px;height:2px;margin:6px auto 0;background:linear-gradient(90deg,transparent,var(--blue-bright),transparent)}
  .reaction{position:absolute;left:30px;top:800px;width:520px;height:184px}
  .reaction-lead{font-size:14px;line-height:1.55;color:var(--ink)}
  .reaction-diagram{position:absolute;left:0;top:56px;width:520px;height:124px}
  .verify{position:absolute;left:574px;top:806px;width:244px;height:174px;border:1.5px solid var(--line);border-radius:4px;text-align:center;padding-top:14px}
  .verify h3{font-size:15px;font-weight:700;color:var(--ink)}
  .verify .marks{display:flex;justify-content:center;gap:18px;margin-top:18px}

  /* footer */
  .footer{position:absolute;left:0;top:1000px;width:846px;height:200px;background:var(--gray);display:flex}
  .provider{flex:1;padding:14px 22px;border-right:2px solid var(--white)}
  .footer-label{font-size:12px;font-weight:700;color:var(--blue-deep)}
  .tech{flex:1;padding:14px 22px}
  .company{display:flex;align-items:center;gap:10px;margin-top:12px}
  .company .mark{width:26px;height:26px;background:var(--blue-deep)}
  .company .name{font-size:20px;font-weight:700;color:var(--blue-deep)}
  .address{font-size:11px;margin-top:8px}
  .contact{display:flex;align-items:center;gap:18px;margin-top:10px}
  .phone{display:flex;align-items:center;gap:6px;font-size:28px;font-weight:900;color:var(--blue-deep);letter-spacing:1px}
  .mail{display:flex;align-items:center;gap:6px;font-size:12px;color:var(--ink)}
</style>
</head>
<body>
<main class="flyer">

  <section class="hero">
    <div class="hero-photo" role="img" aria-label="白い部屋で黄色い手袋をはめ除菌スプレーを向ける、青いエプロン姿の清掃スタッフの写真"></div>

    <div class="service-badge">
      <div class="stars">★★★</div>
      消臭・抗菌<br>施工サービス
    </div>

    <div class="hex-pair">
      <svg viewBox="0 0 250 110" width="250" height="110" aria-hidden="true">
        <defs>
          <linearGradient id="hexFill" x1="0" y1="0" x2="1" y2="1">
            <stop offset="0" stop-color="#ffffff"/>
            <stop offset="1" stop-color="#d3ebf9"/>
          </linearGradient>
        </defs>
        <polygon points="56,18 104,45 104,90 56,100 8,90 8,45" fill="url(#hexFill)" stroke="#8cc6ea" stroke-width="2"/>
        <polygon points="176,2 228,30 228,80 176,106 124,80 124,30" fill="url(#hexFill)" stroke="#8cc6ea" stroke-width="2"/>
      </svg>
      <div class="hex-label alcohol">アルコール</div>
      <div class="hex-label natural">天然由来<br>成分</div>
    </div>

    <div class="power-band"><span><em>2</em>つのチカラで</span></div>
    <h1 class="main-copy">室内除菌</h1>
  </section>

  <section class="scene-row">
    <div class="scene wipe" role="img" aria-label="青い手袋で窓ガラスを拭き掃除する手元の写真"></div>
    <div class="scene room" role="img" aria-label="明るいフローリングの空き部屋の写真"></div>
    <div class="scene family" role="img" aria-label="赤ちゃんを抱く母親の写真"></div>
  </section>

  <h2 class="ingredient-title">アルコールと国産の天然ひのきと緑茶エキスを使用</h2>

  <section class="reaction">
    <p class="reaction-lead">悪臭の原因成分（アンモニア/トリメチルアミン）を<br>ニオイのない成分に変化させます</p>
    <svg class="reaction-diagram" viewBox="0 0 520 124" width="520" height="124" aria-label="中和反応法の図：一般的な消臭剤は包み込むだけ、ひのき・緑茶エキスは悪臭成分を中和し無臭成分へ変える">
      <rect x="0" y="0" width="140" height="122" rx="4" fill="#ffffff" stroke="#c9d6e2"/>
      <rect x="8" y="8" width="90" height="16" rx="2" fill="#8a96a3"/>
      <text x="14" y="20" font-size="10" font-weight="700" fill="#fff" font-family="Noto Sans JP, sans-serif">一般的な消臭剤</text>
      <circle cx="70" cy="68" r="26" fill="#eaf5fc" stroke="#2e9be0" stroke-width="2"/>
      <circle cx="70" cy="68" r="11" fill="#a67c52"/>
      <text x="70" y="112" font-size="9" text-anchor="middle" fill="#333a44" font-family="Noto Sans JP, sans-serif">包み込むだけ</text>

      <rect x="154" y="0" width="366" height="122" rx="4" fill="#ffffff" stroke="#c9d6e2"/>
      <rect x="162" y="8" width="170" height="16" rx="2" fill="#6cb33f"/>
      <text x="168" y="20" font-size="10" font-weight="700" fill="#fff" font-family="Noto Sans JP, sans-serif">ひのき・緑茶エキスの中和反応</text>
      <circle cx="210" cy="68" r="18" fill="#6cb33f"/>
      <text x="210" y="72" font-size="10" font-weight="700" text-anchor="middle" fill="#fff" font-family="Noto Sans JP, sans-serif">成分</text>
      <text x="240" y="74" font-size="18" font-weight="700" text-anchor="middle" fill="#1a78c8">＋</text>
      <circle cx="272" cy="68" r="18" fill="#a67c52"/>
      <text x="272" y="72" font-size="10" font-weight="700" text-anchor="middle" fill="#fff" font-family="Noto Sans JP, sans-serif">悪臭</text>
      <path d="M300 68 H352" stroke="#1a78c8" stroke-width="3"/>
      <polygon points="352,60 366,68 352,76" fill="#1a78c8"/>
      <circle cx="404" cy="68" r="26" fill="#cfe9f8" stroke="#2e9be0" stroke-width="2"/>
      <text x="404" y="72" font-size="11" font-weight="700" text-anchor="middle" fill="#0d4f9c" font-family="Noto Sans JP, sans-serif">無臭</text>
      <text x="336" y="112" font-size="9" text-anchor="middle" fill="#333a44" font-family="Noto Sans JP, sans-serif">悪臭成分を分解し無臭成分に変化</text>
    </svg>
  </section>

  <aside class="verify">
    <h3>第三者機関で効果を検証</h3>
    <div class="marks">
      <svg width="78" height="78" viewBox="0 0 78 78" role="img" aria-label="抗菌製品認証マーク">
        <rect x="2" y="2" width="74" height="74" rx="6" fill="#eaf5fc" stroke="#1a78c8" stroke-width="2"/>
      </svg>
      <svg width="78" height="78" viewBox="0 0 78 78" role="img" aria-label="室内空気衛生推進連盟の認証マーク">
        <circle cx="39" cy="39" r="36" fill="#e4f2d8" stroke="#6cb33f" stroke-width="2"/>
      </svg>
    </div>
  </aside>

  <footer class="footer">
    <div class="provider">
      <p class="footer-label">サービス提供会社</p>
    </div>
    <div class="tech">
      <p class="footer-label">技術提供会社</p>
      <div class="company">
        <span class="mark"></span>
        <span class="name">株式会社住環境企画工房</span>
      </div>
      <p class="address">〒108-0023 東京都港区芝浦4-17-6森田ビル5F</p>
      <div class="contact">
        <span class="phone">
          <svg width="24" height="24" viewBox="0 0 24 24" aria-hidden="true"><path d="M6.6 10.8a15.1 15.1 0 0 0 6.6 6.6l2.2-2.2a1 1 0 0 1 1-.25 11.4 11.4 0 0 0 3.6.57 1 1 0 0 1 1 1V20a1 1 0 0 1-1 1A17 17 0 0 1 3 4a1 1 0 0 1 1-1h3.5a1 1 0 0 1 1 1c0 1.25.2 2.46.57 3.6a1 1 0 0 1-.25 1z" fill="#0d4f9c"/></svg>
          03-5871-2943
        </span>
      </div>
      <p class="mail">
        <svg width="16" height="12" viewBox="0 0 16 12" aria-hidden="true"><rect x="0.5" y="0.5" width="15" height="11" rx="1" fill="none" stroke="#0d4f9c"/><path d="M1 1l7 6 7-6" fill="none" stroke="#0d4f9c"/></svg>
        info@kt-planwork.jp
      </p>
    </div>
  </footer>

</main>
</body>
</html>
```